RUVTOM IT Limited Buisness card logo

I am setting up a IT Consultancy company and want a logo that is related to the IT industry, but also i am thinking that the A in RUV and the A in TOM are linked together maybe horizontally and vertically, also thought about the A being @ as it symbolises IT services. This logo will be used on paperwork, business cards and website.

Industry/Entity Type

Business

Contact Information for Business Card

Gerald Whitmore
RUVTOM IT Limited
IT Consultant
Mobile: 07915362480
Email: geraldvw@mailbryn.co.uk

Requirements
Must have
• IT Theme

```html
<!DOCTYPE html>
<html lang="en">
<head>
<meta charset="utf-8">
<title>RUVTOM IT Limited – Business Card</title>
<link rel="stylesheet" href="https://fonts.googleapis.com/css2?family=PT+Serif:wght@400&display=swap">
<style>
  :root {
    --page-bg: #e9e6e1;
    --card-bg: #080808;
    --card-edge: #1c1c1c;
    --text-light: #b9b9b9;
    --text-muted: #8e8e8e;
    --brand: #b9b9b9;
    --mark-square: #3f7f2e;
    --watermark: #1b1b1b;
    --accent-green: #3e7a2a;
    --accent-blue: #0f4a63;
    --accent-orange: #c4521f;
  }
  html, body {
    margin: 0;
    width: 1200px;
    height: 1000px;
    overflow: hidden;
    background: var(--page-bg);
  }
  .canvas {
    position: relative;
    width: 1200px;
    height: 1000px;
  }
  .card {
    position: absolute;
    left: 150px;
    top: 210px;
    width: 900px;
    height: 580px;
    background: var(--card-bg);
    border-radius: 34px;
    box-shadow: inset 0 0 0 2px var(--card-edge);
    overflow: hidden;
    font-family: "PT Serif", Georgia, serif;
  }
  .brand {
    position: absolute;
    left: 40px;
    top: 44px;
    display: flex;
    align-items: flex-start;
    gap: 20px;
  }
  .brand-square {
    width: 50px;
    height: 50px;
    margin-top: 6px;
    background: var(--mark-square);
  }
  .brand-name {
    margin: 0;
    color: var(--brand);
    font-size: 42px;
    font-weight: 400;
    line-height: 1;
    letter-spacing: 1px;
  }
  .brand-sub {
    margin: 6px 0 0;
    color: var(--brand);
    font-size: 24px;
    font-weight: 400;
    letter-spacing: 3px;
    line-height: 1;
  }
  .at-watermark {
    position: absolute;
    left: 205px;
    top: 40px;
    font-size: 520px;
    line-height: 1;
    color: var(--watermark);
    user-select: none;
  }
  .holder {
    position: absolute;
    left: 0;
    width: 870px;
    top: 268px;
    text-align: center;
  }
  .holder-name {
    margin: 0;
    color: var(--text-light);
    font-size: 36px;
    font-weight: 400;
    line-height: 1;
  }
  .holder-role {
    margin: 10px 0 0;
    color: var(--text-muted);
    font-size: 18px;
    letter-spacing: 12px;
    line-height: 1;
  }
  .contact {
    position: absolute;
    left: 0;
    width: 870px;
    top: 390px;
    text-align: center;
    color: var(--text-light);
    font-size: 26px;
    line-height: 1.35;
  }
  .contact p { margin: 0; }
  .corner-graphic {
    position: absolute;
    right: 0;
    bottom: 0;
    width: 260px;
    height: 280px;
    background: linear-gradient(135deg, var(--accent-green) 0%, var(--accent-blue) 60%, var(--accent-orange) 100%);
    border-top-left-radius: 6px;
  }
</style>
</head>
<body>
  <main class="canvas">
    <article class="card">
      <div class="at-watermark" aria-hidden="true">@</div>

      <header class="brand">
        <div class="brand-square" aria-hidden="true"></div>
        <div>
          <h1 class="brand-name">RUVTOM</h1>
          <p class="brand-sub">IT Limited</p>
        </div>
      </header>

      <section class="holder">
        <h2 class="holder-name">Gerald Whitmore</h2>
        <p class="holder-role">Director</p>
      </section>

      <section class="contact">
        <p>Mobile: 07915362480</p>
        <p>Email: geraldvw@mailbryn.co.uk</p>
      </section>

      <div class="corner-graphic" role="img" aria-label="Decorative corner graphic in green, blue and orange"></div>
    </article>
  </main>
</body>
</html>
```